Keystone Bookkeeping and Tax Services needs a postcard design for his business

Keystone Bookkeeping and Tax Services, specialize in helping small business owners to improve their financial position, maximize their profits as well as helps them to get their lives back. Through proper financial consultation a business can expect to save money on their taxes, use their cash flow effectively, and enjoy a higher return on their business. We would like to have photo of:1. small business owners, 2. an accountant that working. The final design should communicate that by hiring Keystone Bookkeeping and tax services they can concentrate doing their business and relax. Our tag line is "Maximizing your profit is our business". We have our logo already, using blue and orange. The color design should be match with our logo. I upload pictures of small business owner and a logo.
Thanks.

```html
<!DOCTYPE html>
<html lang="en">
<head>
<meta charset="utf-8">
<title>Keystone Bookkeeping and Tax Services – Postcard</title>
<link rel="stylesheet" href="https://fonts.googleapis.com/css2?family=PT+Serif:ital,wght@1,700&family=Roboto+Condensed:wght@400;700&family=Roboto:wght@700&display=swap">
<style>
  :root {
    --page: #ffffff;
    --ink: #111111;
    --blue-dark: #2f7fd0;
    --blue-mid: #4a9ee3;
    --blue-light: #7cc0f0;
    --orange: #f7a21b;
    --yellow: #f6dc2a;
    --navy: #2b3a8f;
    --white: #ffffff;
    --rule: #9a9a9a;
  }
  * { margin: 0; padding: 0; box-sizing: border-box; }
  html, body { width: 848px; height: 1200px; overflow: hidden; background: var(--page); }
  body { position: relative; font-family: "Roboto Condensed", Arial, sans-serif; color: var(--ink); }

  .side-label {
    position: absolute; left: 133px;
    font-family: "Roboto", Arial, sans-serif; font-weight: 700; font-size: 16px;
  }
  .side-label--front { top: 94px; }
  .side-label--back { top: 572px; }

  .card { position: absolute; left: 132px; width: 563px; height: 432px; overflow: hidden; }
  .card--front { top: 120px; }
  .card--back { top: 597px; border: 1px solid var(--rule); background: var(--white); }
  .card-art { position: absolute; inset: 0; width: 100%; height: 100%; }

  .tagline {
    position: absolute; left: 26px; top: 10px;
    font-family: "PT Serif", Georgia, serif; font-style: italic; font-weight: 700;
    font-size: 23px; color: var(--white);
  }
  .brand {
    position: absolute; left: 420px; top: 20px; width: 130px;
    display: flex; flex-direction: column; align-items: center; gap: 8px;
  }
  .brand-mark { width: 34px; height: 34px; background: var(--orange); }
  .brand-name {
    font-family: "Roboto Condensed", Arial, sans-serif; font-weight: 700;
    font-size: 11px; line-height: 13px; color: var(--white); text-align: center;
  }

  .services-title {
    position: absolute; left: 22px; top: 292px;
    font-weight: 700; font-size: 15px; color: var(--white); letter-spacing: .2px;
  }
  .service {
    position: absolute; top: 312px; height: 92px;
    display: flex; flex-direction: column; align-items: center;
    color: var(--white); font-size: 13px; line-height: 14.4px; text-align: center;
  }
  .service svg { width: 24px; height: 26px; margin-bottom: 8px; }
  .service--books { left: 10px; width: 104px; }
  .service--accounts { left: 114px; width: 82px; border-left: 1px solid rgba(255,255,255,.75); }
  .service--tax { left: 196px; width: 86px; border-left: 1px solid rgba(255,255,255,.75); }
  .service--payroll { left: 282px; width: 70px; border-left: 1px solid rgba(255,255,255,.75); }

  .contact {
    position: absolute; left: 389px; top: 348px;
    font-size: 12.5px; line-height: 14.4px; color: var(--white); font-style: normal;
  }

  .benefits { position: absolute; left: 24px; top: 16px; width: 400px; color: var(--navy); }
  .benefits-title { font-weight: 700; font-size: 14.5px; line-height: 18px; }
  .benefits-list { list-style: none; font-size: 12.5px; line-height: 13.4px; }
  .benefits-list li { position: relative; padding-left: 16px; }
  .benefits-list li::before { content: "•"; position: absolute; left: 2px; }
  .benefits-note { margin-top: 14px; font-size: 12px; }
  .stamp-box { position: absolute; left: 442px; top: 34px; width: 84px; height: 84px; background: var(--white); }
</style>
</head>
<body>
  <div class="side-label side-label--front">Front</div>
  <section class="card card--front">
    <svg class="card-art" viewBox="0 0 469 360" preserveAspectRatio="none" aria-hidden="true">
      <defs>
        <linearGradient id="front-bg" x1="0" y1="0" x2="1" y2="1">
          <stop offset="0" stop-color="var(--blue-dark)"/>
          <stop offset="1" stop-color="var(--blue-light)"/>
        </linearGradient>
        <linearGradient id="photo-tone" x1="0" y1="0" x2="1" y2="0">
          <stop offset="0" stop-color="#c9bfb3"/>
          <stop offset=".5" stop-color="#a8a39c"/>
          <stop offset="1" stop-color="#d8cdbf"/>
        </linearGradient>
      </defs>
      <rect width="469" height="360" fill="url(#front-bg)"/>
      <path d="M0,50 Q280,30 469,165 L469,300 Q260,190 0,222 Z" fill="url(#photo-tone)"/>
      <path d="M230,46 Q380,80 469,160" fill="none" stroke="var(--orange)" stroke-width="6"/>
      <path d="M0,222 Q170,205 320,228" fill="none" stroke="var(--yellow)" stroke-width="6"/>
    </svg>
    <div role="img" aria-label="Photo of small business owners reviewing documents with an accountant" style="position:absolute;left:0;top:60px;width:563px;height:200px;"></div>

    <h1 class="tagline">Maximizing your profit&nbsp; is our business</h1>
    <div class="brand">
      <span class="brand-mark"></span>
      <span class="brand-name">KEYSTONE BOOKKEEPING<br>&amp; TAX SERVICES</span>
    </div>

    <h2 class="services-title">SERVICES PROVIDED:</h2>
    <div class="service service--books">
      <svg viewBox="0 0 24 26"><path d="M4 1h11l5 5v19H4z" fill="none" stroke="#fff" stroke-width="1.6"/><text x="12" y="15" font-size="9" font-weight="700" fill="#fff" text-anchor="middle" font-family="Arial">$</text><path d="M8 19h8M8 22h8" stroke="#fff" stroke-width="1.4"/></svg>
      <span>Bookkeeping<br>services to<br>well-organized<br>financial records<br>on a daily basis</span>
    </div>
    <div class="service service--accounts">
      <svg viewBox="0 0 24 26"><rect x="1" y="1" width="22" height="24" fill="none" stroke="#fff" stroke-width="1.6"/><path d="M5 21v-4M9 21v-7M13 21v-9M17 21v-12" stroke="#fff" stroke-width="2.4"/><path d="M4 12 L12 6 L19 4" fill="none" stroke="#fff" stroke-width="1.2"/></svg>
      <span>Accounting<br>Services<br>providing<br>financial<br>information</span>
    </div>
    <div class="service service--tax">
      <svg viewBox="0 0 24 26"><path d="M4 1h11l5 5v19H4z" fill="none" stroke="#fff" stroke-width="1.6"/><text x="11" y="13" font-size="6" font-weight="700" fill="#fff" text-anchor="middle" font-family="Arial">TAX</text><path d="M7 17h10M7 20h10" stroke="#fff" stroke-width="1.4"/></svg>
      <span>Tax Services<br>for Corporate<br>and Personal</span>
    </div>
    <div class="service service--payroll">
      <svg viewBox="0 0 24 26"><path d="M9 3h6l-2 4h-2z" fill="#fff"/><path d="M10 8h4c6 3 8 9 7 13-1 3-4 4-9 4s-8-1-9-4c-1-4 1-10 7-13z" fill="#fff"/><text x="12" y="21" font-size="9" font-weight="700" fill="var(--blue-mid)" text-anchor="middle" font-family="Arial">$</text></svg>
      <span>Payroll<br>Services</span>
    </div>

    <address class="contact">
      118 Harbour Lane,<br>
      Northfield, ON. A1B 2C3<br>
      (555) 014-2730<br>
      info@keystonebooks.ca<br>
      www. KEYSTONEBOOKS.ca
    </address>
  </section>

  <div class="side-label side-label--back">Back</div>
  <section class="card card--back">
    <svg class="card-art" viewBox="0 0 469 360" preserveAspectRatio="none" aria-hidden="true">
      <defs>
        <linearGradient id="back-bg" x1="0" y1="0" x2="1" y2="0">
          <stop offset="0" stop-color="var(--yellow)"/>
          <stop offset="1" stop-color="var(--orange)"/>
        </linearGradient>
      </defs>
      <path d="M0,0 H469 V118 Q240,105 0,130 Z" fill="url(#back-bg)"/>
      <path d="M0,130 Q240,105 469,118 L469,120 Q240,112 0,142 Z" fill="var(--blue-mid)"/>
    </svg>
    <div class="benefits">
      <h2 class="benefits-title">BENEFITS:</h2>
      <ul class="benefits-list">
        <li>We will improve their profit by analyzing Balance Sheet, Profit and Loss Statement, and Key Comparisons to understand and manage trends as well as Assessing their business**</li>
        <li>We will improve your cash flow by **</li>
        <li>We will save your time and money by **</li>
      </ul>
      <p class="benefits-note">** for more detail please contact us</p>
    </div>
    <div class="stamp-box"></div>
  </section>
</body>
</html>
```